Powder Bag Design for supplement company

We need a new bag design for our marine phytoplankton supplement.
we currently have a foil bag with a sticker and we want a full colored design. we are 100% vegan and sustainable. We would want to stick on brand which is a deep blue/purple. (img for reference.) We want a modern updated feel to compete in the market. Playing off of the ocean would be a bonus

Target Market(s)

ages 35+

Industry/Entity Type

health and wellness

```html
<!DOCTYPE html>
<html lang="en">
<head>
<meta charset="UTF-8">
<title>Marlow Pure Marine Phytoplankton Powder – Pouch Front</title>
<link href="https://fonts.googleapis.com/css2?family=Cinzel:wght@500&family=Lobster&family=Montserrat:wght@400;500;600;700&display=swap" rel="stylesheet">
<style>
  :root {
    --navy: #25283f;
    --navy-deep: #1e2039;
    --green: #3aa776;
    --pouch: #f4f4f5;
    --pouch-edge: #e4e5e8;
    --backdrop: #ffffff;
    --ink-soft: #3a3d52;
  }
  html, body {
    margin: 0;
    padding: 0;
    width: 1200px;
    height: 1200px;
    overflow: hidden;
    background: var(--backdrop);
  }
  .canvas {
    position: relative;
    width: 1200px;
    height: 1200px;
  }
  .pouch {
    position: absolute;
    left: 245px;
    top: 38px;
    width: 711px;
    height: 1124px;
    background: var(--pouch);
    border: 1px solid var(--pouch-edge);
    border-radius: 34px 34px 8px 8px;
    overflow: hidden;
  }
  .zip-seal {
    position: absolute;
    left: 0;
    right: 0;
    top: 147px;
    height: 0;
    border-top: 2px solid #e2e3e6;
    border-bottom: 1px solid #fbfbfb;
  }
  .line {
    position: absolute;
    left: 0;
    right: 0;
    text-align: center;
    line-height: 1;
    transform: translateY(-50%);
    white-space: nowrap;
  }
  .brand-name {
    top: 273px;
    font-family: "Montserrat", sans-serif;
    font-weight: 600;
    font-size: 104px;
    color: var(--navy);
    letter-spacing: -1px;
  }
  .brand-tagline {
    top: 375px;
    font-family: "Cinzel", serif;
    font-weight: 500;
    font-size: 15px;
    color: var(--ink-soft);
    letter-spacing: 0.3px;
  }
  .product-kicker {
    font-family: "Cinzel", serif;
    font-weight: 500;
    font-size: 40px;
    color: var(--navy);
  }
  .product-kicker.top { top: 452px; }
  .product-kicker.bottom { top: 575px; }
  .product-name {
    top: 509px;
    font-family: "Lobster", cursive;
    font-size: 66px;
    color: var(--green);
  }
  .leaf-icon {
    position: absolute;
    left: 305px;
    top: 628px;
    width: 104px;
    height: 100px;
  }
  .claim-figure {
    top: 772px;
    font-family: "Montserrat", sans-serif;
    font-weight: 700;
    font-size: 60px;
    color: var(--navy);
  }
  .claim-text {
    top: 826px;
    font-family: "Montserrat", sans-serif;
    font-weight: 600;
    font-size: 29px;
    color: var(--navy);
  }
  .claim-rule {
    position: absolute;
    left: 169px;
    width: 373px;
    top: 858px;
    border-top: 2px solid var(--navy);
  }
  .nutrient-note {
    top: 886px;
    font-family: "Montserrat", sans-serif;
    font-weight: 400;
    font-size: 20px;
    color: var(--navy);
  }
  .nutrient-bold {
    top: 917px;
    font-family: "Montserrat", sans-serif;
    font-weight: 700;
    font-size: 20px;
    color: var(--navy);
  }
  .benefit {
    top: 987px;
    font-family: "Montserrat", sans-serif;
    font-weight: 700;
    font-size: 19px;
    letter-spacing: 2.5px;
    color: var(--green);
  }
  .base-wave {
    position: absolute;
    left: 0;
    bottom: 0;
    width: 711px;
    height: 140px;
  }
  .net-weight {
    position: absolute;
    left: 108px;
    top: 1066px;
    transform: translateY(-50%);
    font-family: "Montserrat", sans-serif;
    font-weight: 700;
    font-size: 21px;
    color: #ffffff;
    line-height: 1;
  }
</style>
</head>
<body>
<main class="canvas">
  <section class="pouch" aria-label="Pouch front">
    <div class="zip-seal"></div>

    <div class="line brand-name">Marlow</div>
    <div class="line brand-tagline">FOR GOOD HEALTH / POUR UNE BONNE SANTÉ</div>

    <div class="line product-kicker top">PURE MARINE</div>
    <div class="line product-name">Phytoplankton</div>
    <div class="line product-kicker bottom">POWDER</div>

    <svg class="leaf-icon" viewBox="0 0 104 100" aria-hidden="true">
      <path d="M40 2 C10 22 4 58 32 92 C44 70 58 40 40 2 Z" fill="var(--green)"/>
      <path d="M102 34 C70 34 44 52 36 96 C70 92 96 70 102 34 Z" fill="var(--green)"/>
      <path d="M36 96 C54 70 74 54 94 42" stroke="var(--pouch)" stroke-width="3" fill="none"/>
    </svg>

    <div class="line claim-figure">100%</div>
    <div class="line claim-text">Vegan And Sustainable</div>
    <div class="claim-rule"></div>
    <div class="line nutrient-note">an excellent source of Zeaxanthin</div>
    <div class="line nutrient-bold">Contains Beta-Carotene</div>

    <div class="line benefit">ANTIOXIDANT</div>

    <svg class="base-wave" viewBox="0 0 711 140" preserveAspectRatio="none" aria-hidden="true">
      <path d="M0 34 C120 10 230 22 340 50 C460 80 600 60 711 20 L711 140 L0 140 Z" fill="var(--navy-deep)"/>
    </svg>
    <div class="net-weight">15g</div>
  </section>
</main>
</body>
</html>
```